Seed Oil Safety Card for Healthy Restaurant Dining

I am seeking a design for a physical card to communicate my wife's health-related dietary restriction regarding seed oils. This card will be given to restaurant waiters to ensure her meals are prepared without seed oils, as it is a health issue and not merely a preference.
My wife cannot eat any “seed oil” or “processed oil”, including:
- Vegetable oil
- Canola oil
- Soybean oil
- Sunflower oil
- Corn oil
- Cottonseed oil
- Safflower oil
- Peanut oil
- Sesame oil
Oils that are OK for her to consume:
- Butter (most preferable)
- Extra virgin olive oil
- Avocado oil
- Coconut oil
- Ghee
- Lard
- Any other animal-based fats
Key Design Requirements:
- Clarity and speed of communication: The card should be easily read and understood by waiters, even in low-light environments, emphasizing that it's a health concern.
- Avoid common misconceptions: Ensure the design doesn't imply common dietary preferences like "vegetarian" or "no butter." Animal fats and butter are actually preferable for her!
- Preferred term: Use "seed oils" as the term to describe what she cannot eat due to her health issue.
- Trace amounts are acceptable: Communicate that it's OK to use cookware that has previously been in contact with seed oils, but not to have seed oil as an ingredient. Please suggest a concise way to convey this.
- Card dimensions: Design should be 3.5” x 2.25” (standard credit-card size on cardlomex.example). Horizontal or vertical layouts are both fine, whichever makes the message clearer.
Design Suggestions:
- Utilize bold and easy-to-read typography to communicate the main message.
- Consider incorporating relevant icons or graphics that help convey the message without adding confusion.
- Use contrasting colors to enhance readability, especially in low-light situations.
- To communicate the “trace amounts OK” part, consider phrases such as:
- "Cross-contamination acceptable"
- “Used cookware OK, no ingredient use”
- “Separate cookware not necessary”
Thank you for your assistance in creating this essential card for my wife's health and safety when dining out!

```html
<!DOCTYPE html>
<html lang="en">
<head>
<meta charset="utf-8">
<title>Medical Dietary Restriction Card</title>
<link href="https://fonts.googleapis.com/css2?family=Lato:ital,wght@0,400;0,700;0,900;1,400&display=swap" rel="stylesheet">
<style>
  :root {
    --page-bg: #e2e3e5;
    --card-bg: #ffffff;
    --brand-blue: #1a6fb0;
    --alert-red: #c8202f;
    --safe-green: #3b8a2f;
    --ink: #222428;
    --mist: #e9ecf1;
  }
  * { box-sizing: border-box; margin: 0; padding: 0; }
  html, body { width: 1200px; height: 2743px; overflow: hidden; }
  body { background: var(--page-bg); font-family: "Lato", sans-serif; position: relative; }

  .card {
    position: absolute; left: 220px; top: 783px; width: 760px; height: 1177px;
    background: var(--card-bg); border-radius: 40px; overflow: hidden;
    box-shadow: 8px 14px 22px rgba(0,0,0,0.28);
    color: var(--ink);
  }
  .card-header {
    position: absolute; left: 0; top: 0; width: 100%; height: 185px;
    background: var(--brand-blue); color: #fff; text-align: center;
    clip-path: polygon(0 0, 100% 0, 100% 163px, 0 185px);
  }
  .card-header .kicker {
    position: absolute; top: 26px; width: 100%;
    font-size: 42px; font-weight: 700; letter-spacing: 9px;
  }
  .card-header .title {
    position: absolute; top: 80px; width: 100%;
    font-size: 54px; font-weight: 900; letter-spacing: 0.5px;
  }

  .emblem-area {
    position: absolute; right: 0; top: 650px; width: 760px; height: 464px;
    background:
      radial-gradient(ellipse 240px 260px at 600px 170px, rgba(214,220,230,0.8), transparent 70%),
      linear-gradient(170deg, transparent 30%, var(--mist) 75%, #dfe3ea 100%);
  }

  .section-icon { position: absolute; width: 64px; height: 64px; }
  .section-heading {
    position: absolute; left: 118px; font-size: 35px; font-weight: 700;
    line-height: 41px; text-transform: uppercase; letter-spacing: 0.3px;
  }

  .oil-list { position: absolute; list-style: none; font-size: 40px; line-height: 47px; }
  .oil-list li { display: flex; align-items: center; }
  .oil-list .box { width: 18px; height: 18px; margin-right: 15px; flex: none; }
  .oil-list--avoid { color: var(--alert-red); }
  .oil-list--safe { color: var(--safe-green); }

  .column-divider {
    position: absolute; left: 366px; top: 298px; width: 7px; height: 224px;
    background: var(--alert-red);
  }

  .trace-note {
    position: absolute; left: 56px; top: 553px; font-size: 33px; font-style: italic;
    line-height: 37px;
  }
  .trace-note span { display: block; padding-left: 14px; }

  .card-footer {
    position: absolute; left: 0; bottom: 0; width: 100%; height: 64px;
    background: var(--brand-blue); color: #fff; text-align: center;
    font-size: 27px; font-weight: 900; letter-spacing: 4px; line-height: 64px;
  }
</style>
</head>
<body>
  <article class="card">
    <header class="card-header">
      <div class="kicker">MEDICAL</div>
      <div class="title">DIETARY RESTRICTION</div>
    </header>

    <div class="emblem-area" role="img" aria-label="Faint medical star of life emblem over a soft grey wave background"></div>

    <svg class="section-icon" style="left:37px; top:200px" viewBox="0 0 64 64" aria-hidden="true">
      <circle cx="32" cy="32" r="31" fill="var(--alert-red)"/>
      <path d="M20 20 L44 44 M44 20 L20 44" stroke="#fff" stroke-width="8" stroke-linecap="round"/>
    </svg>
    <h2 class="section-heading" style="top:212px">I cannot eat processed<br>seed oils</h2>

    <ul class="oil-list oil-list--avoid" style="left:50px; top:296px">
      <li><svg class="box" viewBox="0 0 18 18"><rect x="1" y="1" width="16" height="16" fill="none" stroke="currentColor" stroke-width="2"/><path d="M5 5 L13 13 M13 5 L5 13" stroke="currentColor" stroke-width="2.5"/></svg>Vegetable oil</li>
      <li><svg class="box" viewBox="0 0 18 18"><rect x="1" y="1" width="16" height="16" fill="none" stroke="currentColor" stroke-width="2"/><path d="M5 5 L13 13 M13 5 L5 13" stroke="currentColor" stroke-width="2.5"/></svg>Canola oil</li>
      <li><svg class="box" viewBox="0 0 18 18"><rect x="1" y="1" width="16" height="16" fill="none" stroke="currentColor" stroke-width="2"/><path d="M5 5 L13 13 M13 5 L5 13" stroke="currentColor" stroke-width="2.5"/></svg>Soybean oil</li>
      <li><svg class="box" viewBox="0 0 18 18"><rect x="1" y="1" width="16" height="16" fill="none" stroke="currentColor" stroke-width="2"/><path d="M5 5 L13 13 M13 5 L5 13" stroke="currentColor" stroke-width="2.5"/></svg>Sunflower oil</li>
      <li><svg class="box" viewBox="0 0 18 18"><rect x="1" y="1" width="16" height="16" fill="none" stroke="currentColor" stroke-width="2"/><path d="M5 5 L13 13 M13 5 L5 13" stroke="currentColor" stroke-width="2.5"/></svg>Corn oil</li>
    </ul>
    <div class="column-divider"></div>
    <ul class="oil-list oil-list--avoid" style="left:398px; top:296px">
      <li><svg class="box" viewBox="0 0 18 18"><rect x="1" y="1" width="16" height="16" fill="none" stroke="currentColor" stroke-width="2"/><path d="M5 5 L13 13 M13 5 L5 13" stroke="currentColor" stroke-width="2.5"/></svg>Cottonseed oil</li>
      <li><svg class="box" viewBox="0 0 18 18"><rect x="1" y="1" width="16" height="16" fill="none" stroke="currentColor" stroke-width="2"/><path d="M5 5 L13 13 M13 5 L5 13" stroke="currentColor" stroke-width="2.5"/></svg>Safflower oil</li>
      <li><svg class="box" viewBox="0 0 18 18"><rect x="1" y="1" width="16" height="16" fill="none" stroke="currentColor" stroke-width="2"/><path d="M5 5 L13 13 M13 5 L5 13" stroke="currentColor" stroke-width="2.5"/></svg>Peanut oil</li>
      <li><svg class="box" viewBox="0 0 18 18"><rect x="1" y="1" width="16" height="16" fill="none" stroke="currentColor" stroke-width="2"/><path d="M5 5 L13 13 M13 5 L5 13" stroke="currentColor" stroke-width="2.5"/></svg>Sesame oil</li>
    </ul>

    <p class="trace-note">*Trace amounts acceptable<span>Reuse cookwares acceptable</span></p>

    <svg class="section-icon" style="left:36px; top:673px" viewBox="0 0 64 64" aria-hidden="true">
      <circle cx="32" cy="32" r="31" fill="var(--safe-green)"/>
      <path d="M17 33 L28 44 L47 21" fill="none" stroke="#fff" stroke-width="8" stroke-linecap="round" stroke-linejoin="round"/>
    </svg>
    <h2 class="section-heading" style="top:665px">Natural oils &amp; fats are<br>acceptable</h2>

    <ul class="oil-list oil-list--safe" style="left:50px; top:759px">
      <li><svg class="box" viewBox="0 0 18 18"><rect x="1" y="1" width="16" height="16" fill="none" stroke="currentColor" stroke-width="2"/><path d="M4.5 9 L8 12.5 L14 5" fill="none" stroke="currentColor" stroke-width="2.5"/></svg>Butter</li>
      <li><svg class="box" viewBox="0 0 18 18"><rect x="1" y="1" width="16" height="16" fill="none" stroke="currentColor" stroke-width="2"/><path d="M4.5 9 L8 12.5 L14 5" fill="none" stroke="currentColor" stroke-width="2.5"/></svg>Extra virgin olive oil</li>
      <li><svg class="box" viewBox="0 0 18 18"><rect x="1" y="1" width="16" height="16" fill="none" stroke="currentColor" stroke-width="2"/><path d="M4.5 9 L8 12.5 L14 5" fill="none" stroke="currentColor" stroke-width="2.5"/></svg>Avocado oil</li>
      <li><svg class="box" viewBox="0 0 18 18"><rect x="1" y="1" width="16" height="16" fill="none" stroke="currentColor" stroke-width="2"/><path d="M4.5 9 L8 12.5 L14 5" fill="none" stroke="currentColor" stroke-width="2.5"/></svg>Coconut oil</li>
      <li><svg class="box" viewBox="0 0 18 18"><rect x="1" y="1" width="16" height="16" fill="none" stroke="currentColor" stroke-width="2"/><path d="M4.5 9 L8 12.5 L14 5" fill="none" stroke="currentColor" stroke-width="2.5"/></svg>Ghee</li>
      <li><svg class="box" viewBox="0 0 18 18"><rect x="1" y="1" width="16" height="16" fill="none" stroke="currentColor" stroke-width="2"/><path d="M4.5 9 L8 12.5 L14 5" fill="none" stroke="currentColor" stroke-width="2.5"/></svg>Lard</li>
      <li><svg class="box" viewBox="0 0 18 18"><rect x="1" y="1" width="16" height="16" fill="none" stroke="currentColor" stroke-width="2"/><path d="M4.5 9 L8 12.5 L14 5" fill="none" stroke="currentColor" stroke-width="2.5"/></svg>Natural animal fats</li>
    </ul>

    <footer class="card-footer">THANK YOU FOR KEEPING ME SAFE</footer>
  </article>
</body>
</html>
```